website refresh with jungle and/or gorilla theme for marketing agency

Our marketing agency needs a creative website boost. The website (which is Wordpress) is:https://www.tallreedmedia.com. Given our name, we would like to have a jungle/gorilla theme. The Tallreed website should have a beastly presence. See the site now and how the gorilla is in your face. The text can remain the same, we just need a new layout and/or graphics. What other direction can I give? Not sure, we will know it when we see it.

Target Market(s)

small and medium sized businesses

Industry/Entity Type

Digital Marketing

Number of Pages Required

1 page

Colors

Designer to choose colors to be used in the design.

Requirements
Must have
• I don't really have any must have's. I don't want to limit the creativity of the designer.
Nice to have
• I am encouraging an out of the box design, something that isn't so "boxy" and traditional like the other sites.
Should not have
• I don't like standard looking sites that have a boxy layout with your standard cartoon and/or basic icons.

```html
<!DOCTYPE html>
<html lang="en">
<head>
<meta charset="utf-8">
<title>Tallreed Marketing</title>
<link href="https://fonts.googleapis.com/css2?family=Londrina+Solid:wght@400;900&family=Open+Sans:wght@400;600;700&display=swap" rel="stylesheet">
<style>
:root{
  --ink:#000;
  --band:#1d1d1d;
  --blue:#4ea6dc;
  --white:#fff;
  --muted:#cfcfcf;
  --gold:#f4b223;
  --orange:#f7a01b;
  --field:#111;
  --line:#8a8a8a;
}
*{box-sizing:border-box;margin:0;padding:0}
html,body{width:1200px;height:2903px;overflow:hidden;background:var(--ink)}
body{position:relative;font-family:'Open Sans',sans-serif;color:var(--white)}
.abs{position:absolute}
.display{font-family:'Londrina Solid',sans-serif;font-weight:900;color:var(--blue)}

/* hero */
.hero-photo{left:0;top:0;width:1200px;height:860px;
  background:radial-gradient(ellipse 60% 45% at 50% 62%,#3a3a3a 0%,#1c1c1c 45%,#070707 100%)}
.brand{left:0;width:1200px;top:48px;text-align:center}
.brand span{display:inline-block;font-family:'Londrina Solid',sans-serif;font-weight:900;font-size:40px;color:var(--blue);letter-spacing:1px}
.nav{left:0;width:1200px;top:170px;display:flex;justify-content:center;gap:46px;
  font-family:'Londrina Solid',sans-serif;font-weight:900;font-size:25px;letter-spacing:3px;text-transform:uppercase}
.nav a{color:var(--white);text-decoration:none}
.nav a.current{color:var(--blue)}
.hero-title{left:0;width:1200px;top:240px;text-align:center;line-height:1}
.hero-title .l1{display:block;font-size:76px;letter-spacing:2px}
.hero-title .l2{display:block;font-size:62px;letter-spacing:3px;margin-top:4px}
.hero-sub{left:0;width:1200px;top:402px;text-align:center;font-size:16px;font-weight:600}
.cta{left:531px;top:463px;width:148px;height:40px;border-radius:6px;background:var(--gold);
  color:#111;font-weight:700;font-size:16px;display:flex;align-items:center;justify-content:center}

/* why */
.why-title{left:232px;top:880px;font-size:44px;letter-spacing:1px}
.why-copy{left:232px;top:950px;width:412px;font-size:12.5px;line-height:18px;color:var(--muted)}
.why-copy p+p{margin-top:18px}
.video{left:676px;top:852px;width:384px;height:230px}
.video-photo{position:absolute;inset:0;background:linear-gradient(135deg,#e8e8e8,#6d6d6d 55%,#222);border-radius:60px 90px 40px 70px}
.play{position:absolute;left:162px;top:96px;width:56px;height:40px;border:3px solid var(--white);border-radius:8px}
.more-videos{left:790px;top:1098px;display:flex;align-items:center;gap:14px;font-size:25px;letter-spacing:1px}
.more-videos svg{display:block}
.divider{left:364px;top:1196px;width:530px;border-top:2px dashed #555}

/* dogs */
.dogs-line{left:242px;top:1230px;font-size:34px;line-height:44px;letter-spacing:1px}
.dogs-num{left:658px;top:1218px;font-size:104px;line-height:1;letter-spacing:2px}
.dogs-note{left:846px;top:1253px;width:200px;font-size:13px;line-height:17px;color:var(--muted)}

/* about band */
.band{left:0;top:1340px;width:1200px;height:600px}
.about-photo{left:194px;top:1440px;width:310px;height:360px;border-radius:40px 30px 50px 20px;
  background:radial-gradient(ellipse at 50% 45%,#5a5550 0%,#2b2826 55%,#141414 100%)}
.about-title{left:538px;top:1432px;font-family:'Londrina Solid',sans-serif;font-weight:900;font-size:40px;color:var(--white)}
.about-copy{left:538px;top:1496px;width:490px;font-size:12.5px;line-height:18px;color:var(--muted)}
.about-copy p+p{margin-top:18px}
.benefit{top:1672px;width:170px;font-family:'Londrina Solid',sans-serif;font-weight:900;font-size:24px;line-height:25px;color:var(--white)}
.benefit svg{display:block;margin:0 0 8px 6px}

/* testimonial */
.say-title{left:0;width:1200px;top:1918px;text-align:center;font-size:30px;letter-spacing:1px}
.quote{left:0;width:1200px;top:1978px;text-align:center;font-size:22px;line-height:29px;color:var(--white)}
.quote-by{left:0;width:1200px;top:2057px;text-align:center;font-size:14px;color:var(--blue)}
.avatar{left:538px;top:2092px;width:112px;height:112px;border-radius:50%;border:3px solid #555;
  background:linear-gradient(160deg,#cfcfcf,#5c5c5c)}

/* footer zone */
.foot-photo{left:0;top:2560px;width:1200px;height:343px;
  background:radial-gradient(ellipse 45% 60% at 50% 30%,#3b3330 0%,#161311 55%,#000 100%)}
.brands-title{left:230px;top:2265px;font-size:36px;line-height:44px;letter-spacing:1px}
.partner{font-family:'Open Sans',sans-serif;color:var(--white);display:flex;align-items:center;gap:10px}
.contact-title{left:662px;top:2262px;font-size:38px;letter-spacing:1px}
.contact-info{left:662px;top:2320px;width:420px;font-size:21px;line-height:28px;color:var(--muted)}
.field{position:absolute;height:36px;border:1px solid var(--line);background:var(--field);
  font-size:11px;color:var(--muted);padding:10px 16px}
.field.filled{color:var(--white);font-size:13px;font-weight:600;padding-top:9px}
.send{left:662px;top:2568px;width:288px;height:42px;background:var(--orange);
  display:flex;align-items:center;justify-content:center;font-weight:700;font-size:14px;letter-spacing:.5px}
.foot-links{left:228px;top:2750px;display:flex;gap:14px;font-size:10px;text-transform:uppercase;color:var(--white)}
.copyright{left:228px;top:2784px;font-size:10px;text-transform:uppercase;color:var(--white)}
.social{left:918px;top:2768px;display:flex;gap:16px}
.social span{width:16px;height:16px;border-radius:50%;background:var(--white)}
</style>
</head>
<body>

<!-- hero -->
<div class="abs hero-photo" role="img" aria-label="Close-up of a gorilla's brow and eyes staring from darkness"></div>
<div class="abs brand"><span>Tallreed Marketing</span></div>
<nav class="abs nav">
  <a class="current">Home</a><a>About</a><a>Learn</a><a>Portfolio</a><a>Contact</a>
</nav>
<h1 class="abs hero-title display">
  <span class="l1">Social and Search</span>
  <span class="l2">Marketing Beasts</span>
</h1>
<p class="abs hero-sub">Get performance driven digital marketing leaders on your team</p>
<div class="abs cta">Get Started</div>

<!-- why -->
<h2 class="abs why-title display">Why Tallreed Marketing?</h2>
<div class="abs why-copy">
  <p>Tallreed Marketing is the apex predator of the Social and Search marketing industries. We are senior marketing experts with the skills to create revenue-producing marketing funnels. In this age of big data, there is no better way to earn instant visibility with your audience than to have a REAL team of skilled pros on your side.</p>
  <p>Is your marketing funnel maximizing revenue and conversions? Learn the single biggest mistake companies make in their marketing funnel and how to fix it.</p>
</div>
<div class="abs video">
  <div class="video-photo" role="img" aria-label="Black and white video still of the agency founder speaking"></div>
  <div class="play"><svg width="50" height="34" viewBox="0 0 50 34"><path d="M20 9 L32 17 L20 25Z" fill="#fff"/></svg></div>
</div>
<div class="abs more-videos display">
  <svg width="30" height="24" viewBox="0 0 30 24"><rect x="2" y="2" width="26" height="20" rx="3" fill="none" stroke="#4ea6dc" stroke-width="3"/><path d="M12 7 L20 12 L12 17Z" fill="#4ea6dc"/></svg>
  <span><span style="color:var(--blue)">MORE</span> <span style="color:var(--white)">VIDEOS</span></span>
</div>
<div class="abs divider"></div>

<!-- dogs -->
<p class="abs dogs-line display">In 2017, we helped 962<br>dogs. In 2018 we helped...</p>
<p class="abs dogs-num display">220</p>
<p class="abs dogs-note">abused and/or homeless dogs through the Palm Paws rescue fund.</p>

<!-- about band -->
<svg class="abs band" viewBox="0 0 1200 600" preserveAspectRatio="none" aria-hidden="true">
  <path d="M0 20 L140 8 L300 26 L470 2 L640 22 L820 0 L990 18 L1200 6 L1200 560 L1060 590 L880 566 L700 596 L520 570 L340 598 L170 574 L0 592Z" fill="#1d1d1d"/>
</svg>
<div class="abs about-photo" role="img" aria-label="Portrait of a silverback gorilla looking forward"></div>
<h2 class="abs about-title">About Us</h2>
<div class="abs about-copy">
  <p>What sets us apart from other marketing agencies is our team of A-players. Each team member has proven themselves to be in the top 1% of all marketers. They are the 1 percenters who are passionate about what they do and have proven experience to back up their incredible skill sets.</p>
  <p>Led by Dana Carrow, who has built and sold 4 companies himself and written 5 books (one best-seller), the team at Tallreed Marketing specializes in user acquisition, lead generation, and brand visibility.</p>
</div>
<div class="abs benefit" style="left:551px">
  <svg width="80" height="70" viewBox="0 0 80 70"><circle cx="40" cy="18" r="12" fill="#fff"/><circle cx="16" cy="26" r="9" fill="#fff"/><circle cx="64" cy="26" r="9" fill="#fff"/><path d="M22 66 Q22 36 40 36 Q58 36 58 66Z" fill="#fff"/><path d="M2 62 Q2 40 16 40 Q24 40 26 48 L22 62Z" fill="#fff"/><path d="M78 62 Q78 40 64 40 Q56 40 54 48 L58 62Z" fill="#fff"/></svg>
  Get More<br>Traffic
</div>
<div class="abs benefit" style="left:688px">
  <svg width="74" height="70" viewBox="0 0 74 70"><circle cx="37" cy="35" r="28" fill="none" stroke="#fff" stroke-width="5"/><circle cx="37" cy="35" r="16" fill="#fff"/><circle cx="37" cy="4" r="4" fill="#fff"/><circle cx="68" cy="35" r="4" fill="#fff"/><circle cx="6" cy="35" r="4" fill="#fff"/><circle cx="37" cy="66" r="4" fill="#fff"/></svg>
  Higher Quality<br>Leads
</div>
<div class="abs benefit" style="left:880px">
  <svg width="100" height="64" viewBox="0 0 100 64"><rect x="2" y="8" width="60" height="40" fill="none" stroke="#fff" stroke-width="5"/><rect x="12" y="16" width="40" height="24" fill="#fff"/><ellipse cx="82" cy="14" rx="14" ry="6" fill="#fff"/><rect x="68" y="20" width="28" height="8" fill="#fff"/><rect x="68" y="32" width="28" height="8" fill="#fff"/><rect x="68" y="44" width="28" height="8" fill="#fff"/></svg>
  Get More<br>Sales
</div>

<!-- testimonial -->
<h2 class="abs say-title display">What say people about us</h2>
<p class="abs quote">“The team at Tallreed Marketing truly love what they do.<br>They are fast, accurate and responsive.”</p>
<p class="abs quote-by">Owen Marsh, Founder, Second Leash Rescue</p>
<div class="abs avatar" role="img" aria-label="Round portrait photo of the client"></div>

<!-- brands and contact -->
<div class="abs foot-photo" role="img" aria-label="Dark close-up of a gorilla's open mouth and teeth"></div>
<h2 class="abs brands-title display">Name Brands We've<br>Worked For</h2>
<div class="abs partner" style="left:230px;top:2380px;font-size:24px;line-height:26px">Loomwell<br>Apparel</div>
<div class="abs partner" style="left:392px;top:2392px;font-size:24px;font-weight:700"><span style="width:26px;height:26px;background:#fff;display:inline-block"></span>Harborline</div>
<div class="abs partner" style="left:230px;top:2450px;font-size:22px"><span style="width:30px;height:30px;border-radius:50%;background:#fff;display:inline-block"></span>Meridian Telecom</div>

<h2 class="abs contact-title display">Contact Tallreed Marketing</h2>
<p class="abs contact-info">555-014-2290, 48 Fernridge Ct,<br>&nbsp;Alder Bay CA 90000</p>
<div class="field filled" style="left:662px;top:2382px;width:158px">James|</div>
<div class="field" style="left:836px;top:2382px;width:160px">Last Name</div>
<div class="field" style="left:662px;top:2432px;width:158px">Email Address</div>
<div class="field" style="left:836px;top:2432px;width:160px">Phone Number</div>
<div class="field" style="left:662px;top:2482px;width:334px;height:76px;padding-top:8px">Description Message</div>
<div class="abs send">SEND IT TO ME!</div>

<!-- footer -->
<div class="abs foot-links"><span>Home</span><span>About</span><span>Learn</span><span>Portfolio</span><span>Contact</span><span>Privacy Policy</span><span>Terms and Conditions</span></div>
<p class="abs copyright">Copyright Tallreed Marketing All Rights Reserved</p>
<div class="abs social" aria-label="Social links"><span></span><span></span><span></span><span></span></div>

</body>
</html>
```